creation of a business card design for a company specializing in the creation...

I would like to create a design for a professional business card on a black background and with the company's colors (I am attaching some files: including the logo in horizontal and centered format, I am also attaching a recent project design a T-shirt, this is the one I chose to give you an idea of my preferences.

we are in the process of developing a new website design, it is still in the development phase but it can be viewed at the following address: www.vendrelak.be to give you other ideas about the company
you will see for yourself the subject of my main activity: company specializing in the construction of stairs

I would like a business card that stands out from the rest with a unique design

here is the informations
Name: Florent Dubrec
Function: Manager
Address: Rue Masquelin du Pont 41
7180 La Louvière
telephone: +32 486 219 508
email: info@rv8k.be
website: rv8k. be
social networks: Facebook, YouTube, TikTok, Instagram

Target Market(s)

customer who wants to have a beautiful staircase built

Industry/Entity Type

contruction d'escalier

Contact Information for Business Card

Adresse. Numero de telephone, site web, le texte : "Createur d'escalier", logo recto-verso, icone des reseaux sociaux

Requirements
Must have
• the mention: Stair creator
Nice to have
• an illustration of a designer staircase
Should not have
• do not distort the logo

```html
<!DOCTYPE html>
<html lang="en">
<head>
<meta charset="utf-8">
<title>RV8K business card</title>
<link href="https://fonts.googleapis.com/css2?family=Montserrat:wght@400;500;700&display=swap" rel="stylesheet">
<style>
  :root {
    --scene: #151517;
    --card: #1d1e20;
    --edge: #6e9dbd;
    --accent: #6f9fc0;
    --accent-light: #9cbfd6;
    --text: #f2f3f4;
    --muted-mark: #34353a;
    --white: #ffffff;
  }
  * { box-sizing: border-box; margin: 0; padding: 0; }
  html, body {
    width: 1200px; height: 900px; overflow: hidden;
    background: var(--scene);
    font-family: "Montserrat", sans-serif;
  }
  .canvas {
    width: 1200px; height: 900px;
    display: flex; flex-direction: column; align-items: center; justify-content: center;
    gap: 44px;
  }
  .card {
    position: relative;
    width: 660px; height: 377px;
    background: var(--card);
    border-radius: 22px;
    border-bottom: 4px solid var(--edge);
    overflow: hidden;
  }

  .brand-block { display: flex; flex-direction: column; align-items: flex-end; }
  .brand { display: flex; align-items: center; gap: 18px; }
  .brand-square { width: 54px; height: 54px; }
  .brand-name { font-weight: 500; font-size: 78px; letter-spacing: 10px; line-height: 1; }
  .tagline {
    font-weight: 400; text-transform: uppercase; white-space: nowrap;
    line-height: 1;
  }

  /* front */
  .card-front { display: flex; align-items: center; justify-content: center; }
  .card-front .brand-square { background: var(--muted-mark); }
  .card-front .brand-name { color: var(--muted-mark); }
  .card-front .tagline {
    color: var(--muted-mark); font-size: 13px; letter-spacing: 8px;
    margin-top: 12px; margin-right: 2px;
  }

  /* back */
  .card-back .brand-block { position: absolute; left: 62px; top: 150px; }
  .card-back .brand { gap: 12px; }
  .card-back .brand-square { width: 36px; height: 36px; background: var(--accent-light); }
  .card-back .brand-name { color: var(--text); font-size: 48px; letter-spacing: 6px; }
  .card-back .tagline {
    color: var(--text); font-size: 9px; letter-spacing: 4.5px; margin-top: 9px;
  }

  .divider {
    position: absolute; left: 318px; top: 70px;
    width: 2px; height: 190px; background: var(--white);
  }
  .contact { position: absolute; left: 345px; top: 66px; color: var(--text); }
  .contact-name { color: var(--accent); font-weight: 700; font-size: 26px; line-height: 1.1; }
  .contact-role { font-size: 15px; margin-bottom: 18px; }
  .contact-address { font-size: 15px; line-height: 1.35; margin-bottom: 16px; }
  .contact-list { list-style: none; font-size: 15px; line-height: 1.5; }
  .contact-list li { display: flex; align-items: center; gap: 12px; }
  .contact-list svg { width: 14px; height: 14px; fill: var(--accent-light); }

  .social { position: absolute; left: 430px; top: 282px; display: flex; gap: 12px; }
  .social-dot { width: 16px; height: 16px; border-radius: 50%; background: var(--accent-light); }

  .bands { position: absolute; left: 0; bottom: 0; width: 660px; height: 80px; }
</style>
</head>
<body>
<main class="canvas">
  <section class="card card-front" aria-label="Card front">
    <div class="brand-block">
      <div class="brand">
        <span class="brand-square"></span>
        <span class="brand-name">RV8K</span>
      </div>
      <p class="tagline">Stair creator</p>
    </div>
  </section>

  <section class="card card-back" aria-label="Card back">
    <div class="brand-block">
      <div class="brand">
        <span class="brand-square"></span>
        <span class="brand-name">RV8K</span>
      </div>
      <p class="tagline">Stair creator</p>
    </div>

    <span class="divider"></span>

    <div class="contact">
      <p class="contact-name">Florent Dubrec</p>
      <p class="contact-role">Manager</p>
      <p class="contact-address">Rue Masquelin du Pont 41<br>7180 La Louvière</p>
      <ul class="contact-list">
        <li>
          <svg viewBox="0 0 24 24" aria-hidden="true"><path d="M6.6 10.8a15.1 15.1 0 0 0 6.6 6.6l2.2-2.2c.3-.3.7-.4 1-.2 1.1.4 2.3.6 3.6.6.6 0 1 .4 1 1V20c0 .6-.4 1-1 1A17 17 0 0 1 3 4c0-.6.4-1 1-1h3.5c.6 0 1 .4 1 1 0 1.3.2 2.5.6 3.6.1.3 0 .7-.2 1z"/></svg>
          +32 486 219 508
        </li>
        <li>
          <svg viewBox="0 0 24 24" aria-hidden="true"><path d="M2 5h20v14H2z M2 5l10 8 10-8"/></svg>
          info@rv8k.be
        </li>
        <li>
          <svg viewBox="0 0 24 24" aria-hidden="true"><circle cx="12" cy="12" r="10"/></svg>
          www.rv8k.be
        </li>
      </ul>
    </div>

    <div class="social" role="img" aria-label="Social network links">
      <span class="social-dot"></span>
      <span class="social-dot"></span>
      <span class="social-dot"></span>
      <span class="social-dot"></span>
    </div>

    <svg class="bands" viewBox="0 0 660 80" aria-hidden="true">
      <polygon points="0,44 430,44 400,80 0,80" fill="var(--accent)"/>
      <polygon points="460,30 660,0 660,26 490,48 448,48" fill="var(--white)"/>
    </svg>
  </section>
</main>
</body>
</html>
```